Steady Yield Fund

Need to design a h: 200 w: 260mm advert for print publishing. The product is an investment fund that pays monthly cash distributions.

Background on product:
https://tarnwellcapital.com.au/our-funds/steady-yield-smallcap-fund/

NEWSPRINT TECHNICAL SPECIFICATIONS
The following are print specifications to assist the preparation and creation of PDF artwork files for Newsprint advertising for the above mentioned publications.

Image Resolution
We print at a linescreen ruling of 100 lpi. Please supply at a minimum of:

Images: 150 dpi
Single bitmap: 600 dpi
Logos supplied as either single bitmap or vector artwork.

Colour
Colour should be supplied as CMYK.

Total Ink Coverage
Ensure all elements including TIFFs, JPEGs, or EPS images do not exceed (CMYK) 240% total ink.

Fonts and Type
It is not recommend reversing text out of four colour images. Minimum type sizes are:

Single solid colour: 6 pt
Coloured type on a white background using two or three colour plates: 8 pt
Reversed type out of one colour plates: 8 pt
Reversed type out of two or more colour plates: 12 pt san serif, bold

```html
<!DOCTYPE html>
<html lang="en">
<head>
<meta charset="utf-8">
<title>Steady Yield Value Smallcap Fund</title>
<link href="https://fonts.googleapis.com/css2?family=Poppins:wght@400;700&display=swap" rel="stylesheet">
<style>
  :root {
    --ink: #1c1b1a;
    --gold: #d4a64a;
    --tone-figure: #6b6b6b;
    --tone-wall: #8a8a8a;
    --tone-alley: #cfcfcf;
    --tone-alley-edge: #c2c2c2;
    --tone-sky: #f8f8f8;
  }
  html, body {
    margin: 0;
    padding: 0;
    width: 1200px;
    height: 923px;
    overflow: hidden;
    background: #ffffff;
  }
  .advert {
    position: relative;
    width: 1200px;
    height: 923px;
    overflow: hidden;
    font-family: "Poppins", sans-serif;
  }
  .hero-photo {
    position: absolute;
    inset: 0;
    background:
      linear-gradient(180deg, rgba(248,248,248,0.95) 0%, rgba(248,248,248,0) 16%) 570px 0 / 380px 923px no-repeat,
      linear-gradient(180deg, rgba(0,0,0,0.06) 0%, rgba(0,0,0,0) 40%, rgba(255,255,255,0.05) 100%),
      linear-gradient(90deg,
        var(--tone-wall) 0%,
        #7a7a7a 8%,
        var(--tone-figure) 22%,
        #646464 40%,
        #767676 50%,
        #a8a8a8 57%,
        #c4c4c4 64%,
        var(--tone-alley) 80%,
        var(--tone-alley-edge) 100%);
  }
  .headline {
    position: absolute;
    right: 88px;
    top: 102px;
    margin: 0;
    text-align: right;
    color: var(--ink);
    font-weight: 700;
    font-size: 70px;
    line-height: 72px;
    letter-spacing: -0.5px;
  }
  .subhead {
    position: absolute;
    right: 88px;
    top: 254px;
    margin: 0;
    text-align: right;
    color: var(--gold);
    font-weight: 400;
    font-size: 35px;
    line-height: 50px;
  }
  .brand {
    position: absolute;
    right: 88px;
    top: 706px;
    margin: 0;
    text-align: right;
  }
  .brand-name {
    display: block;
    color: var(--gold);
    font-weight: 700;
    font-size: 54px;
    line-height: 58px;
  }
  .brand-descriptor {
    display: block;
    margin-top: 8px;
    color: var(--ink);
    font-weight: 400;
    font-size: 19px;
    line-height: 24px;
  }
</style>
</head>
<body>
  <main class="advert">
    <div class="hero-photo" role="img" aria-label="Black-and-white photograph of a smiling man in a dark suit and tie standing in a city laneway"></div>

    <h1 class="headline">Steady Yield Value<br>Smallcap Fund</h1>

    <p class="subhead">For wholesale investors looking<br>for regular cash income</p>

    <p class="brand">
      <span class="brand-name">Tarnwell<br>Capital</span>
      <span class="brand-descriptor">Tarnwell Capital Management</span>
    </p>
  </main>
</body>
</html>
```